Marlowick APP redesign and color change

I am looking for a new design for my app. Please see the attached current design.

Currently, I have a functioning app but the colors and design are awful!
The logo is great but the rest of the app needs a refresh.
(Logo hi res not yet available but will upload soon.)
New colors or anything that is cutting edge.

Basically: It is a secure social media app within a school system where the teachers, students and parents can text, exchange photos, plan curriculum, etc.

I NEED ONLY landing page with a new look!
Looking for one distinct design for the landing page with new look.
The developer will apply this one design towards the rest of the pages/app screens.

Because part of the social media I need the feel and look of what is now the trend. Something that will attract and keep the client(s) interested. I am really leaving all the creative work to the designer and open to any suggestions.
Updates

Target Market(s)

Schools, community, teachers, students, colleges, sport teams

Industry/Entity Type

Non Profit

Font styles to use
Serif
Sans Serif

Colors

Designer to choose colors to be used in the design.

Requirements
Must have
• Sharp, trendy, millennial feel
Nice to have
• Up to designer
Should not have
• Up to designer

```html
<!DOCTYPE html>
<html lang="en">
<head>
<meta charset="utf-8">
<title>Marlowick – App Screens</title>
<link rel="stylesheet" href="https://fonts.googleapis.com/css2?family=Fira+Sans+Condensed:wght@400;500&family=Open+Sans:wght@400;600&display=swap">
<style>
:root{
  --bg:#222222;
  --screen:#f6f7f7;
  --field:#ffffff;
  --line:#e4e6e7;
  --text:#3a3d40;
  --muted:#9a9ea2;
  --teal:#2fb5a4;
  --blue:#1f6e9a;
  --grad:linear-gradient(100deg,var(--teal),var(--blue));
  --avatar:#c9a892;
}
*{box-sizing:border-box;margin:0;padding:0}
html,body{width:1200px;height:800px;overflow:hidden;background:var(--bg)}
body{font-family:"Fira Sans Condensed",sans-serif;color:var(--text)}
.row{position:absolute;left:31px;top:213px;display:flex;gap:22px}
.screen{position:relative;width:210px;height:374px;background:var(--screen);overflow:hidden;border-radius:3px}
.status{position:absolute;top:0;left:0;right:0;height:16px;display:flex;justify-content:space-between;align-items:center;padding:0 7px;font:500 7px "Open Sans",sans-serif;color:var(--text)}
.status.light{color:#fff}
.title{position:absolute;left:0;right:0;text-align:center;font-size:11px;line-height:15px;color:#6c7074}
.title b{font-weight:500;color:var(--text)}
.field{position:absolute;left:14px;right:14px;height:38px;background:var(--field);border:1px solid var(--line);font-size:9px;color:var(--muted);padding:13px 12px}
.check{position:absolute;left:14px;right:14px;display:flex;align-items:center;gap:6px;font-size:7.5px;color:var(--text)}
.check .aside{margin-left:auto}
.btn{position:absolute;left:14px;right:14px;height:34px;background:var(--grad);color:#fff;font-size:10.5px;display:flex;align-items:center;justify-content:center;box-shadow:0 3px 6px rgba(0,0,0,.18)}
.foot{position:absolute;left:0;right:0;text-align:center;font-size:7px;color:var(--text)}
.foot em{font-style:normal;color:var(--teal)}
.brand{position:absolute;top:82px;left:0;right:0;display:flex;justify-content:center;align-items:center;gap:7px}
.brand-dot{width:10px;height:10px;border-radius:50%;background:var(--teal)}
.brand-name{font:600 17px "Open Sans",sans-serif;color:var(--teal)}
.tagline{position:absolute;top:108px;left:0;right:0;text-align:center;font:400 8px "Open Sans",sans-serif;color:var(--text)}
.prompt{position:absolute;top:290px;left:0;right:0;text-align:center;font:400 8px "Open Sans",sans-serif;color:var(--text)}
.cta{position:absolute;top:312px;width:80px;height:32px;font:600 9.5px "Open Sans",sans-serif;display:flex;align-items:center;justify-content:center}
.cta.primary{left:20px;background:var(--grad);color:#fff;box-shadow:0 3px 6px rgba(0,0,0,.2)}
.cta.ghost{right:20px;border:1.5px solid var(--blue);color:var(--blue)}
.appbar{position:absolute;top:0;left:0;right:0;height:62px;background:var(--grad)}
.appbar .back{position:absolute;left:8px;top:34px;color:#fff;font-size:8px}
.appbar .icons{position:absolute;right:10px;top:30px;display:flex;gap:8px}
.search{position:absolute;top:62px;left:0;right:0;height:24px;background:#fff;border-bottom:1px solid var(--line);font-size:7.5px;color:var(--muted);display:flex;align-items:center;gap:6px;padding:0 10px}
.list{position:absolute;top:86px;left:0;right:0}
.contact{height:42px;background:#fff;border-bottom:1px solid var(--line);display:flex;align-items:center;padding:0 10px;gap:8px}
.avatar{width:24px;height:24px;border-radius:50%;background:var(--avatar);flex:none}
.contact .who{flex:1}
.contact .name{font-size:8px;font-weight:500}
.contact .msg{font-size:6.5px;color:var(--muted)}
.dot{width:16px;height:16px;border-radius:50%;background:var(--teal);position:relative}
.dot::after{content:"";position:absolute;left:5px;top:5px;width:6px;height:6px;border-radius:50%;background:#fff}
.tabbar{position:absolute;bottom:0;left:0;right:0;height:36px;background:var(--grad);display:flex;justify-content:space-around;align-items:center}
.chatbar{position:absolute;top:0;left:0;right:0;height:48px;background:var(--grad);color:#fff;font-size:11px;padding:24px 10px 0}
.time{position:absolute;top:60px;left:0;right:0;text-align:center;font-size:6.5px;color:var(--teal)}
.bubble{position:absolute;font-size:6.5px;padding:6px 8px}
.bubble.in{left:24px;background:var(--teal);color:#fff}
.bubble.out{right:24px;background:#fff;color:var(--text);box-shadow:0 1px 3px rgba(0,0,0,.1)}
.mini{position:absolute;width:12px;height:12px;border-radius:50%;background:var(--avatar)}
.media{position:absolute;top:170px;left:24px;right:24px;height:110px;background:#fff;box-shadow:0 1px 4px rgba(0,0,0,.12)}
.media .photo{height:94px;background:linear-gradient(135deg,#e8ecef,#b7c2c9)}
.media .track{position:absolute;bottom:7px;left:8px;right:8px;height:2px;background:var(--line)}
.media .track::before{content:"";position:absolute;left:0;width:40%;height:2px;background:var(--teal)}
.compose{position:absolute;bottom:0;left:0;right:0;height:46px;background:#fff;border-top:1px solid var(--line);display:flex;align-items:center;gap:6px;padding:0 10px;font-size:7px;color:var(--muted)}
.compose span{flex:1}
.round{width:16px;height:16px;border-radius:50%;background:var(--teal)}
</style>
</head>
<body>
<main class="row">

  <section class="screen login">
    <div class="status"><span>●●●○○ NIMBUS</span><span>4:21 PM</span><span>22%</span></div>
    <p class="title" style="top:84px">You are just One Step<br><b>Go To Sign In</b></p>
    <div class="field" style="top:130px">Username</div>
    <div class="field" style="top:180px">Password</div>
    <div class="check" style="top:236px">
      <svg width="8" height="8" viewBox="0 0 8 8"><path d="M1 4l2 2 4-5" fill="none" stroke="#3a3d40" stroke-width="1.3"/></svg>
      <span>Remember me</span><span class="aside">Forgot Password</span>
    </div>
    <div class="btn" style="top:266px">Sign In</div>
    <p class="foot" style="top:318px">Create a account? <em>Sign up</em></p>
  </section>

  <section class="screen signup">
    <div class="status"><span>●●●○○ NIMBUS</span><span>4:21 PM</span><span>22%</span></div>
    <p class="title" style="top:72px">You are New Here<br><b>Please Sign Up</b></p>
    <div class="field" style="top:116px">Username</div>
    <div class="field" style="top:164px">Password</div>
    <div class="field" style="top:212px">Confirm Password</div>
    <div class="check" style="top:266px">
      <svg width="8" height="8" viewBox="0 0 8 8"><path d="M1 4l2 2 4-5" fill="none" stroke="#3a3d40" stroke-width="1.3"/></svg>
      <span>Accept Terms &amp; Conditions</span>
    </div>
    <div class="btn" style="top:292px">Sign Up Now</div>
    <p class="foot" style="top:344px">Already have an account? <em>Sign up</em></p>
  </section>

  <section class="screen landing">
    <div class="status"><span>●●●○○ NIMBUS</span><span>4:21 PM</span><span>22%</span></div>
    <div class="brand"><span class="brand-dot"></span><h1 class="brand-name">Marlowick</h1></div>
    <p class="tagline">Safe messaging for every school</p>
    <p class="prompt">Create a new account or sign in</p>
    <a class="cta primary">Get Started</a>
    <a class="cta ghost">Sign In</a>
  </section>

  <section class="screen conversations">
    <header class="appbar">
      <div class="status light"><span>●●●○○ NIMBUS</span><span>4:21 PM</span><span>22%</span></div>
      <span class="back">‹ Back</span>
      <div class="icons">
        <svg width="11" height="11" viewBox="0 0 11 11"><circle cx="5.5" cy="5.5" r="4.5" fill="none" stroke="#fff" stroke-width="1.4"/></svg>
        <svg width="11" height="11" viewBox="0 0 11 11"><circle cx="4.5" cy="4.5" r="3.5" fill="none" stroke="#fff" stroke-width="1.4"/><path d="M7 7l3 3" stroke="#fff" stroke-width="1.4"/></svg>
      </div>
    </header>
    <div class="search">
      <svg width="8" height="8" viewBox="0 0 11 11"><circle cx="4.5" cy="4.5" r="3.5" fill="none" stroke="#2fb5a4" stroke-width="1.4"/><path d="M7 7l3 3" stroke="#2fb5a4" stroke-width="1.4"/></svg>
      Search Conversations...
    </div>
    <div class="list">
      <div class="contact"><div class="avatar" role="img" aria-label="Profile photo of Nora Vance"></div><div class="who"><p class="name">Nora Vance</p><p class="msg">Hlo How Are You?</p></div><div class="dot"></div></div>
      <div class="contact"><div class="avatar" role="img" aria-label="Profile photo of Milo Herrera"></div><div class="who"><p class="name">Milo Herrera</p><p class="msg">Tonight I am Going Home</p></div><div class="dot"></div></div>
      <div class="contact"><div class="avatar" role="img" aria-label="Profile photo of Owen Reyes"></div><div class="who"><p class="name">Owen Reyes</p><p class="msg">So Whats Going on There</p></div><div class="dot"></div></div>
      <div class="contact"><div class="avatar" role="img" aria-label="Profile photo of Ada Ross"></div><div class="who"><p class="name">Ada Ross</p><p class="msg">Hlo All Things is Working</p></div><div class="dot"></div></div>
      <div class="contact"><div class="avatar" role="img" aria-label="Profile photo of Theo Marsh"></div><div class="who"><p class="name">Theo Marsh</p><p class="msg">Amazing App Design</p></div><div class="dot"></div></div>
      <div class="contact"><div class="avatar" role="img" aria-label="Profile photo of Clara Webb"></div><div class="who"><p class="name">Clara Webb</p><p class="msg">This Gonna Be Rock</p></div><div class="dot"></div></div>
    </div>
    <nav class="tabbar">
      <svg width="12" height="12" viewBox="0 0 12 12"><rect x="1" y="2" width="10" height="7" fill="none" stroke="#fff" stroke-width="1.2"/></svg>
      <svg width="12" height="12" viewBox="0 0 12 12"><g fill="none" stroke="#fff" stroke-width="1.2"><rect x="1" y="1" width="4" height="4"/><rect x="7" y="1" width="4" height="4"/><rect x="1" y="7" width="4" height="4"/><rect x="7" y="7" width="4" height="4"/></g></svg>
      <svg width="12" height="12" viewBox="0 0 12 12"><rect x="2" y="1" width="8" height="10" fill="none" stroke="#fff" stroke-width="1.2"/></svg>
      <svg width="12" height="12" viewBox="0 0 12 12"><circle cx="6" cy="6" r="4" fill="none" stroke="#fff" stroke-width="1.2"/><circle cx="6" cy="6" r="1.5" fill="#fff"/></svg>
    </nav>
  </section>

  <section class="screen chat">
    <header class="chatbar">
      <div class="status light"><span>●●●○○ NIMBUS</span><span>4:21 PM</span><span>22%</span></div>
      ‹ Nora Vance
    </header>
    <p class="time">9:20 PM</p>
    <div class="mini" style="left:8px;top:80px" role="img" aria-label="Avatar of Nora Vance"></div>
    <p class="bubble in" style="top:76px">Hlo How Are You ?</p>
    <div class="mini" style="right:8px;top:112px" role="img" aria-label="Avatar of the user"></div>
    <p class="bubble out" style="top:110px">I'm Fine You Say Dear</p>
    <div class="mini" style="left:8px;top:146px" role="img" aria-label="Avatar of Nora Vance"></div>
    <p class="bubble in" style="top:142px">Please send me video :D</p>
    <figure class="media">
      <div class="photo" role="img" aria-label="Shared video thumbnail of a portrait with bold makeup"></div>
      <div class="track"></div>
    </figure>
    <footer class="compose"><span>Type here...</span><i class="round"></i><i class="round"></i><i class="round"></i></footer>
  </section>

</main>
</body>
</html>
```